The Larchmont Fitters

We need a business card design for our wardrobe company.
Please visit our website www.glimmerbayinteriors.com to get an idea of who we are.

```html
<!DOCTYPE html>
<html lang="en">
<head>
<meta charset="utf-8">
<title>The Larchmont Fitters – Business Card</title>
<link href="https://fonts.googleapis.com/css2?family=Montserrat:wght@600&family=Roboto:wght@400;500&family=Roboto+Condensed:wght@400&display=swap" rel="stylesheet">
<style>
  :root {
    --backdrop: #d9d9d9;
    --card-white: #ffffff;
    --card-dark: #1c1b1a;
    --ink: #1a1a1a;
    --ink-soft: #444444;
    --rule: #2b2b2b;
    --on-dark: #ffffff;
    --shadow: rgba(0, 0, 0, 0.22);
  }
  * { box-sizing: border-box; margin: 0; padding: 0; }
  html, body {
    width: 1200px;
    height: 930px;
    overflow: hidden;
    background: var(--backdrop);
  }
  .sheet {
    position: relative;
    width: 1200px;
    height: 930px;
  }
  .card {
    position: absolute;
    left: 260px;
    width: 680px;
    height: 388px;
    border-radius: 26px;
    overflow: hidden;
    box-shadow: 0 8px 22px var(--shadow);
  }
  .card--back { top: 55px; background: var(--card-dark); }
  .card--front { top: 487px; background: var(--card-white); }

  .back-photo {
    position: absolute;
    inset: 0;
    background:
      linear-gradient(180deg, #3a3836 0%, #252321 30%, #1a1918 65%, #2a2725 100%);
  }
  .back-photo::after {
    content: "";
    position: absolute;
    inset: 0;
    background: radial-gradient(ellipse at 55% 55%, rgba(120,110,100,0.18), rgba(0,0,0,0) 60%);
  }

  .brand {
    position: absolute;
    display: flex;
    align-items: center;
    gap: 16px;
  }
  .brand-mark {
    width: 34px;
    height: 34px;
    border: 2px solid currentColor;
    flex: none;
  }
  .brand-name {
    font-family: "Montserrat", sans-serif;
    font-weight: 600;
    font-size: 19px;
    letter-spacing: 0.3px;
    text-transform: uppercase;
    line-height: 1.2;
  }
  .brand-tagline {
    font-family: "Montserrat", sans-serif;
    font-weight: 600;
    font-size: 15px;
    margin-top: 6px;
  }
  .card--back .brand { left: 180px; top: 160px; color: var(--on-dark); }
  .card--front .brand { left: 150px; top: 58px; color: var(--ink); }

  .rule {
    position: absolute;
    height: 1px;
    background: var(--rule);
  }
  .rule--top { left: 370px; right: 36px; top: 132px; }
  .rule--bottom { left: 36px; right: 36px; top: 290px; }

  .person {
    position: absolute;
    left: 330px;
    top: 168px;
    text-align: center;
    width: 300px;
    color: var(--ink);
  }
  .person-name {
    font-family: "Roboto", sans-serif;
    font-weight: 500;
    font-size: 31px;
    letter-spacing: 0.5px;
  }
  .person-role {
    font-family: "Roboto", sans-serif;
    font-size: 14px;
    color: var(--ink-soft);
    margin-top: 2px;
  }

  .contacts {
    position: absolute;
    left: 36px;
    right: 36px;
    top: 304px;
    text-align: center;
    font-family: "Roboto Condensed", sans-serif;
    font-size: 17px;
    color: var(--ink);
    line-height: 1.6;
  }
</style>
</head>
<body>
<main class="sheet">
  <section class="card card--back" aria-label="Card back">
    <div class="back-photo" role="img" aria-label="Dim photograph of a walk-in wardrobe with shelves of hanging clothes"></div>
    <div class="brand">
      <span class="brand-mark"></span>
      <div>
        <p class="brand-name">The Larchmont Fitters</p>
        <p class="brand-tagline">Fitted Right, Room by Room</p>
      </div>
    </div>
  </section>

  <section class="card card--front" aria-label="Card front">
    <div class="brand">
      <span class="brand-mark"></span>
      <div>
        <p class="brand-name">The Larchmont Fitters</p>
        <p class="brand-tagline">Fitted Right, Room by Room</p>
      </div>
    </div>
    <div class="rule rule--top"></div>
    <div class="person">
      <p class="person-name">DANIEL HARTLEY</p>
      <p class="person-role">Director</p>
    </div>
    <div class="rule rule--bottom"></div>
    <div class="contacts">
      <p>P : 0207 555 0148 | E : info@glimmerbayinteriors.com | W : www.glimmerbayinteriors.com</p>
      <p>A : Orchard House, 42 Fenmore Street, London EC2A 4PL</p>
    </div>
  </section>
</main>
</body>
</html>
```